velturi.org business card design

We need 2-sided business cards for velturi.org; one side will be printed in English (EN), the other in Spanish (ES); the information represnted will be the same.
We are a non-profit that aims to mentor and coach future leaders / visionaries. Our target markets are developing countries (Latin America, Africa, Asia) rather than the developed ("western") world. Our business model works by finding funding to mentor / coach a candidate. We provide several mentors / coaches per candidate which help translate the candidate's vision / dream into a path with objectives and steps.
We want the business cards to transmit our values, which are: innovation, learning / self-improvement, equality (i.e. free from discrimination), boldness, intelligence, thoughtfulness, culture, society, future, sustainability.
We recommend the designers work with these values to produce a bold and innovative design, which does not need to adhere to the traditional criteria for business cards. Please use fresh (modern) colours.

Target Market(s)

Visionaries and thought leaders all over the world, but initially in Latin America. We don't discriminate on age, sex, religion, race or any other difference between people

Industry/Entity Type

Leadership

Contact Information for Business Card

The business cards will contain one language (English / Spanish) per side. It would be nice to have some continuity between the front and the back (e.g. pattern, colours).
Each side will contain the company name, website (www.velturi.org) and a slogan / mantra (which will be provided and can be represented as a placeholder until such time). The other details will be Name, (Function), and contact details (email and phone number).

Font styles to use
Sans Serif

Colors

Designer to choose colors to be used in the design.

Requirements
Must have
• [Side A: ENGLISH --- COMPANY INFO]
• [Company Name] Velturi
• [Slogan / Mantra] Shape your world!
• [Website] velturi.org
• [Side A: ENGLISH --- PERSONAL INFO]
• [Name] Dan Pilcher
• [Job Title] Mentoring Coordinator
• [Phone / WhatsApp] +51 947 218 306
• [eMail] dan@velturi.org
• [Side B: SPANISH --- COMPANY INFO]
• [Company Name] Velturi
• [Slogan / Mantra] ¡Moldea tu mundo!
• [Website] velturi.org
• [Side B: SPANISH --- PERSONAL INFO]
• [Name] Daniel Pilcher
• [Job Title] Coordinador de Mentoreo
• [eMail] dan@velturi.org
• [SIDE A: ENGLISH --- Central Values]
• - Future
• - Growth
• - Leadership
• [SIDE B: SPANISH --- Central Values]
• - Futuro
• - Liderazgo
• - Crecimiento
Nice to have
• Innovative and different design. Modern and fresh. Bold and clever.
• Secondary Values (we would like represented) are:
• [SIDE A: ENGLISH --- Secondary Values]
• - Equality
• - Innovation
• - Sustainability
• [SIDE B: SPANISH --- Secondary Values]
• - Igualdad
• - Innovación
• - Sostenibilidad
Should not have
• Please note that the images I have attached to this brief are just some images that I liked while browsing for material for the website. It does not imply I want these colours or this type of design, just that I felt these images had a good feel.

```html
<!DOCTYPE html>
<html lang="en">
<head>
<meta charset="utf-8">
<title>Velturi business cards</title>
<link rel="stylesheet" href="https://fonts.googleapis.com/css2?family=Open+Sans:wght@300;400;700&family=Tinos&display=swap">
<style>
  :root {
    --backdrop: #2f2926;
    --card-white: #fbfbfa;
    --brand-blue: #1b80bd;
    --brand-green: #5cb82e;
    --ink: #3a3a3a;
    --ink-soft: #555;
    --on-blue: #ffffff;
  }
  * { box-sizing: border-box; margin: 0; padding: 0; }
  html, body { width: 1200px; height: 844px; overflow: hidden; }
  body {
    background: var(--backdrop);
    font-family: "Open Sans", Arial, sans-serif;
    position: relative;
  }
  .card {
    position: absolute;
    top: 267px;
    width: 540px;
    height: 310px;
    border-radius: 3px;
    box-shadow: 0 10px 26px rgba(0,0,0,.45);
  }
  .card--english { left: 40px; background: var(--card-white); color: var(--ink); }
  .card--spanish { left: 620px; background: var(--brand-blue); color: var(--on-blue); }

  .brand {
    position: absolute;
    top: 36px;
    right: 42px;
    display: flex;
    align-items: center;
    gap: 10px;
    font-weight: 300;
    font-size: 56px;
    letter-spacing: 2px;
    line-height: 1;
  }
  .card--english .brand { color: var(--brand-blue); }
  .brand-dot { width: 12px; height: 12px; border-radius: 50%; background: var(--brand-green); }
  .card--spanish .brand-dot { background: var(--on-blue); }

  .person { position: absolute; left: 38px; top: 116px; }
  .person-name { font-weight: 700; font-size: 21px; letter-spacing: .3px; line-height: 24px; }
  .card--english .person-name { color: var(--brand-blue); }
  .person-role { font-size: 14px; line-height: 20px; margin: 1px 0 0 10px; color: var(--ink-soft); }
  .card--spanish .person-role { color: rgba(255,255,255,.85); }

  .contacts { list-style: none; margin: 10px 0 0 24px; }
  .contacts li { display: flex; align-items: center; gap: 7px; font-size: 15px; line-height: 22px; }
  .contacts svg { width: 15px; height: 15px; flex: none; }

  .values { position: absolute; left: 62px; bottom: 22px; font-size: 15px; line-height: 20px; letter-spacing: .3px; }
  .values .sep { margin: 0 7px; color: var(--brand-blue); }
  .card--spanish .values .sep { color: var(--on-blue); }

  .slogan {
    position: absolute;
    right: 38px;
    bottom: 86px;
    font-family: "Tinos", "Times New Roman", serif;
    font-size: 20px;
    line-height: 24px;
    letter-spacing: .5px;
  }
  .card--english .slogan { color: var(--brand-green); }
</style>
</head>
<body>

<section class="card card--english" aria-label="English side">
  <div class="brand"><span class="brand-dot"></span>Velturi</div>

  <div class="person">
    <h1 class="person-name">DANIEL PILCHER</h1>
    <p class="person-role">Coordinator Mentoring</p>
    <ul class="contacts">
      <li><svg viewBox="0 0 16 16"><circle cx="8" cy="8" r="7" fill="none" stroke="#1b80bd" stroke-width="1.6"/></svg>+51 947 218 306</li>
      <li><svg viewBox="0 0 16 16"><circle cx="8" cy="8" r="8" fill="#1b80bd"/><path d="M5 4.5l1.6-.4 1 2-1 .8a5 5 0 0 0 2.5 2.5l.8-1 2 1-.4 1.6c-3.3.3-6.8-3.2-6.5-6.5z" fill="#fff"/></svg>+51 947 218 306</li>
      <li><svg viewBox="0 0 16 16"><circle cx="8" cy="8" r="8" fill="#1b80bd"/><rect x="4" y="5.2" width="8" height="5.6" rx=".6" fill="#fff"/><path d="M4.3 5.6L8 8.4l3.7-2.8" fill="none" stroke="#1b80bd" stroke-width=".9"/></svg>dan@velturi.org</li>
    </ul>
  </div>

  <p class="values">Growth<span class="sep">|</span>Future<span class="sep">|</span>Leadership</p>
  <p class="slogan">SHAPE YOUR WORLD!</p>
</section>

<section class="card card--spanish" aria-label="Spanish side" lang="es">
  <div class="brand"><span class="brand-dot"></span>Velturi</div>

  <div class="person">
    <h2 class="person-name">DANIEL PILCHER</h2>
    <p class="person-role">Coordinador de Mentoreo</p>
    <ul class="contacts">
      <li><svg viewBox="0 0 16 16"><circle cx="8" cy="8" r="7" fill="none" stroke="#fff" stroke-width="1.6"/></svg>+51 947 218 306</li>
      <li><svg viewBox="0 0 16 16"><circle cx="8" cy="8" r="8" fill="#fff"/><path d="M5 4.5l1.6-.4 1 2-1 .8a5 5 0 0 0 2.5 2.5l.8-1 2 1-.4 1.6c-3.3.3-6.8-3.2-6.5-6.5z" fill="#1b80bd"/></svg>+51 947 218 306</li>
      <li><svg viewBox="0 0 16 16"><circle cx="8" cy="8" r="8" fill="#fff"/><rect x="4" y="5.2" width="8" height="5.6" rx=".6" fill="#1b80bd"/><path d="M4.3 5.6L8 8.4l3.7-2.8" fill="none" stroke="#fff" stroke-width=".9"/></svg>dan@velturi.org</li>
    </ul>
  </div>

  <p class="values">Crecimiento<span class="sep">|</span>Futuro<span class="sep">|</span>Liderazgo</p>
  <p class="slogan">MOLDEA TU MUNDO!</p>
</section>

</body>
</html>
```